Spark of Meadow Paddocks Business Cards with logo

Need a creative business card that pops. Colorful but professional. The attached logo should be included. We are a national horse racing partnership so we are in the equine business. Nothing cartoonlike or whimsical.

Target Market(s)

professionals - 40+

Contact Information for Business Card

Dana Whitlow
Director of Operations
27 Pinecrest Lane
Middletown, MD. 21769

Phone (555) 274-6183

FX: (555) 619-3047

email: dana@smpaddocks.example
smpaddocks.example

Requirements
Must have
• All information above should be on the business card including the website address. Professional yet creative
Nice to have
• an attention grabbing design. not boring. exciting.
Should not have
• cartoon like - whimsical.

```html
<!DOCTYPE html>
<html lang="en">
<head>
<meta charset="utf-8">
<title>Spark of Meadow Paddocks – Business Card</title>
<link rel="stylesheet" href="https://fonts.googleapis.com/css2?family=Open+Sans:wght@300;400;600;700&display=swap">
<style>
  :root {
    --page-bg: #f2f2f2;
    --card-white: #ffffff;
    --gold: #c6901e;
    --gold-soft: #dcb25a;
    --navy: #0b2a6b;
    --text-light: #ffffff;
  }
  * { margin: 0; padding: 0; box-sizing: border-box; }
  html, body {
    width: 1200px;
    height: 960px;
    overflow: hidden;
    background: var(--page-bg);
    font-family: "Open Sans", Arial, sans-serif;
  }
  .business-card {
    position: absolute;
    left: 100px;
    top: 210px;
    width: 1000px;
    height: 541px;
    background: var(--card-white);
    overflow: hidden;
  }
  .card-art {
    position: absolute;
    inset: 0;
    width: 100%;
    height: 100%;
  }
  .contact-block {
    position: absolute;
    left: 66px;
    top: 185px;
    color: var(--text-light);
  }
  .person-name {
    font-size: 24px;
    font-weight: 700;
    line-height: 30px;
  }
  .person-title,
  .address-line {
    font-size: 22px;
    font-weight: 300;
    line-height: 30px;
  }
  .address { margin-top: 20px; }
  .contact-lines {
    position: absolute;
    right: 670px;
    top: 380px;
    text-align: right;
    color: var(--text-light);
    font-size: 17px;
    font-weight: 300;
    line-height: 31.5px;
  }
  .contact-lines b { font-weight: 700; }
  .brand-mark {
    position: absolute;
    left: 713px;
    top: 58px;
    width: 224px;
    height: 224px;
    border: 2px solid var(--gold);
    border-radius: 50%;
    display: flex;
    align-items: center;
    justify-content: center;
    text-align: center;
  }
  .brand-name {
    color: var(--navy);
    font-size: 22px;
    font-weight: 700;
    line-height: 28px;
    letter-spacing: 0.5px;
  }
  .website {
    position: absolute;
    right: 57px;
    top: 488px;
    color: var(--text-light);
    font-size: 27px;
    font-weight: 600;
    letter-spacing: 0.6px;
    line-height: 36px;
  }
</style>
</head>
<body>
  <article class="business-card">
    <svg class="card-art" viewBox="0 0 824 446" preserveAspectRatio="none" aria-hidden="true">
      <defs>
        <linearGradient id="rider-tone" x1="0" y1="0" x2="0" y2="1">
          <stop offset="0" stop-color="var(--gold-soft)"/>
          <stop offset="1" stop-color="var(--gold)"/>
        </linearGradient>
      </defs>
      <polygon class="gold-panel" points="0,4 376,202 300,446 0,446" fill="var(--gold)"/>
      <rect class="rider-image" role="img" aria-label="Silhouette of a rider on a jumping horse"
            x="384" y="60" width="160" height="300" rx="10" fill="url(#rider-tone)"/>
      <polygon class="navy-stripe" points="4,0 60,0 378,152 376,202"
               fill="var(--navy)" stroke="var(--card-white)" stroke-width="3" stroke-linejoin="round"/>
      <path class="navy-footer" d="M345,446 C380,405 430,390 490,390 L824,390 L824,446 Z" fill="var(--navy)"/>
    </svg>

    <div class="contact-block">
      <p class="person-name">Dana Whitlow</p>
      <p class="person-title">Director of Operations</p>
      <div class="address">
        <p class="address-line">27 Pinecrest Lane</p>
        <p class="address-line">Middletown, MD. 21769</p>
      </div>
    </div>

    <div class="contact-lines">
      <p><b>Phone</b> (555) 274-6183</p>
      <p><b>FX:</b> (555) 619-3047</p>
      <p><b>email:</b> dana@smpaddocks.example</p>
    </div>

    <div class="brand-mark">
      <p class="brand-name">Spark of Meadow<br>Paddocks</p>
    </div>

    <p class="website">www.smpaddocks.example</p>
  </article>
</body>
</html>
```